Criação de Papelaria (6 itens) para Beleza
" Somos uma Distribuidora de Cosméticos. Compramos os produtos diretamente das Indústrias e depois revendemos para lojistas em MG e no Norte do Rio. Antes, nós éramos uma distribuidora apenas da marca Vorani (https://www.voranicosmeticos.com.br/). Por esse motivo, utilizávamos uma logo feita pelo marketing deles, nas cores deles, para que as duas logos sempre andassem casadas. Hoje, ampliamos o nosso mix e distribuímos também os produtos da Mirtex ( https://www.mirtex.com.br/) e da henna Sol de Jade. Ou seja, hoje somos efetivamente uma distribuidora de Cosméticos em geral, atendendo os michos de cabelo, pele, maquiagem e unhas. Dessa maneira, criamos uma nova logo, para representar a Distribuidora. "

```html
<!DOCTYPE html>
<html lang="pt-BR">
<head>
<meta charset="UTF-8">
<title>Lumera — Blocos de Anotação</title>
<link href="https://fonts.googleapis.com/css2?family=Montserrat:wght@400;500;600;700&display=swap" rel="stylesheet">
<style>
  :root {
    --stage: #2b2c2f;
    --paper: #ffffff;
    --rule: #d9dbdf;
    --ink: #2a2d33;
    --ink-soft: #6b6f77;
    --gold: #c9a24a;
    --navy-top: #1f2836;
    --navy-bottom: #0c1017;
    --ghost: #eef0f2;
  }
  * { box-sizing: border-box; margin: 0; padding: 0; }
  html, body { width: 1200px; height: 1200px; overflow: hidden; }
  body {
    background: var(--stage);
    font-family: "Montserrat", sans-serif;
    position: relative;
  }
  .sheet {
    position: absolute;
    width: 372px;
    height: 500px;
    background: var(--paper);
    overflow: hidden;
    box-shadow: 0 10px 30px rgba(0,0,0,.35);
  }
  .sheet--lined { left: 456px; top: 72px; }
  .sheet--blank { left: 220px; top: 630px; }
  .sheet--cover {
    left: 608px; top: 630px;
    background: linear-gradient(160deg, var(--navy-top), var(--navy-bottom));
  }
  .ghost-ring {
    position: absolute;
    left: 20px; top: 40px;
    width: 370px; height: 370px;
    border-radius: 50%;
    border: 42px solid var(--ghost);
  }
  .sheet--cover .ghost-ring {
    border-color: rgba(255,255,255,.04);
    left: -130px; top: 70px;
  }
  .brand { position: absolute; display: flex; align-items: center; gap: 6px; white-space: nowrap; }
  .brand__dot { width: 18px; height: 18px; border-radius: 50%; background: var(--gold); flex: none; }
  .brand__name { font-weight: 600; font-size: 17px; letter-spacing: 1px; color: var(--ink); line-height: 1; }
  .brand__tag { font-weight: 600; font-size: 5px; letter-spacing: .5px; color: var(--ink); margin-top: 2px; }
  .sheet--lined .brand { left: 16px; top: 18px; }
  .header-rule {
    position: absolute; left: 150px; right: 16px; top: 42px;
    height: 2px; background: var(--ink);
  }
  .lines {
    position: absolute; left: 16px; right: 16px; top: 62px; height: 384px;
    background: repeating-linear-gradient(to bottom, transparent 0 11px, var(--rule) 11px 12px);
  }
  .sheet--blank .brand { left: 16px; bottom: 44px; }
  .sheet--cover .brand {
    left: 50%; top: 50%; transform: translate(-50%, -50%);
    gap: 10px;
  }
  .sheet--cover .brand__dot { width: 32px; height: 32px; }
  .sheet--cover .brand__name { font-size: 30px; color: #ffffff; letter-spacing: 2px; }
  .sheet--cover .brand__tag { font-size: 7px; color: #ffffff; letter-spacing: 1px; }
  .contacts {
    position: absolute; left: 16px; right: 16px; bottom: 14px;
    display: flex; justify-content: space-between; align-items: center;
    font-size: 5px; color: var(--ink-soft); font-weight: 500; white-space: nowrap;
  }
  .contact { display: flex; align-items: center; gap: 4px; line-height: 1.4; }
  .contact svg { width: 9px; height: 9px; flex: none; }
</style>
</head>
<body>

<section class="sheet sheet--lined">
  <div class="ghost-ring"></div>
  <div class="brand">
    <span class="brand__dot"></span>
    <div>
      <div class="brand__name">LUMERA</div>
      <div class="brand__tag">DISTRIBUIDORA DE COSMÉTICOS</div>
    </div>
  </div>
  <div class="header-rule"></div>
  <div class="lines"></div>
  <footer class="contacts">
    <div class="contact">
      <svg viewBox="0 0 10 10"><circle cx="5" cy="5" r="5" fill="#2a2d33"/><path d="M5 2.2a1.7 1.7 0 0 1 1.7 1.7C6.7 5.2 5 7.6 5 7.6S3.3 5.2 3.3 3.9A1.7 1.7 0 0 1 5 2.2z" fill="#fff"/></svg>
      <span>Av. das Acácias, 240 - Centro<br>Contagem - MG - CEP 32000-000</span>
    </div>
    <div class="contact">
      <svg viewBox="0 0 10 10"><circle cx="5" cy="5" r="5" fill="#2a2d33"/><path d="M3.3 2.6l1 1-.5.7a3.5 3.5 0 0 0 1.9 1.9l.7-.5 1 1-.6.8C5.2 7.4 2.6 4.8 2.5 3.2z" fill="#fff"/></svg>
      <span>(31) 3000-0000</span>
    </div>
    <div class="contact">
      <svg viewBox="0 0 10 10"><circle cx="5" cy="5" r="5" fill="#2a2d33"/><rect x="2.6" y="3.3" width="4.8" height="3.4" fill="#fff"/><path d="M2.6 3.3L5 5.2l2.4-1.9" stroke="#2a2d33" stroke-width=".5" fill="none"/></svg>
      <span>contato@lumera.com.br</span>
    </div>
  </footer>
</section>

<section class="sheet sheet--blank">
  <div class="ghost-ring"></div>
  <div class="brand">
    <span class="brand__dot"></span>
    <div>
      <div class="brand__name">LUMERA</div>
      <div class="brand__tag">DISTRIBUIDORA DE COSMÉTICOS</div>
    </div>
  </div>
  <footer class="contacts">
    <div class="contact">
      <svg viewBox="0 0 10 10"><circle cx="5" cy="5" r="5" fill="#2a2d33"/><path d="M5 2.2a1.7 1.7 0 0 1 1.7 1.7C6.7 5.2 5 7.6 5 7.6S3.3 5.2 3.3 3.9A1.7 1.7 0 0 1 5 2.2z" fill="#fff"/></svg>
      <span>Av. das Acácias, 240 - Centro<br>Contagem - MG - CEP 32000-000</span>
    </div>
    <div class="contact">
      <svg viewBox="0 0 10 10"><circle cx="5" cy="5" r="5" fill="#2a2d33"/><path d="M3.3 2.6l1 1-.5.7a3.5 3.5 0 0 0 1.9 1.9l.7-.5 1 1-.6.8C5.2 7.4 2.6 4.8 2.5 3.2z" fill="#fff"/></svg>
      <span>(31) 3000-0000</span>
    </div>
    <div class="contact">
      <svg viewBox="0 0 10 10"><circle cx="5" cy="5" r="5" fill="#2a2d33"/><rect x="2.6" y="3.3" width="4.8" height="3.4" fill="#fff"/><path d="M2.6 3.3L5 5.2l2.4-1.9" stroke="#2a2d33" stroke-width=".5" fill="none"/></svg>
      <span>contato@lumera.com.br</span>
    </div>
  </footer>
</section>

<section class="sheet sheet--cover">
  <div class="ghost-ring"></div>
  <div class="brand">
    <span class="brand__dot"></span>
    <div>
      <div class="brand__name">LUMERA</div>
      <div class="brand__tag">DISTRIBUIDORA DE COSMÉTICOS</div>
    </div>
  </div>
</section>

</body>
</html>
```